Brightwater Medical business cards

Double sided business cards.

Medical technology consulting company.

Business cards with two names on the front, upper to middle left:

Dr Colin R. Haskell MBBS FRACGP +61491578204
Dr Paul Brennagh PhD MBusStrategy +61472019847

Email and website addresses bottom right:

colin@brightwatermedical.com.au
www.brightwatermedical.com.au

Tree logo (as per attached file) on front in a suitable position.

Tag line (as per attached files) on the back.

Need a file format to upload to Desk Ford or Cardmoor.

```html
<!DOCTYPE html>
<html lang="en">
<head>
<meta charset="utf-8">
<title>Brightwater Medical – Business Cards</title>
<link href="https://fonts.googleapis.com/css2?family=Lato:wght@400;700&display=swap" rel="stylesheet">
<style>
  :root {
    --backdrop: #727272;
    --card-white: #ffffff;
    --card-cream: #fff1d6;
    --leaf-green: #4b7f1f;
    --tag-green: #4a8a35;
    --maroon: #6b0f0f;
    --soft-leaf: #7fae76;
    --soft-bark: #9b4e4c;
    --shadow: rgba(0,0,0,0.45);
  }
  * { margin: 0; padding: 0; box-sizing: border-box; }
  html, body { width: 1200px; height: 1000px; overflow: hidden; }
  body {
    background: var(--backdrop);
    font-family: "Lato", "Helvetica Neue", Arial, sans-serif;
    position: relative;
  }
  .card {
    position: absolute;
    left: 294px;
    width: 613px;
    height: 352px;
    overflow: hidden;
    box-shadow: 14px 16px 22px var(--shadow);
  }
  .card--front {
    top: 128px;
    background: var(--card-white);
    border-radius: 56px 0 56px 0;
  }
  .card--back {
    top: 522px;
    background: var(--card-cream);
    border-radius: 0 56px 0 56px;
  }
  .front-artwork {
    position: absolute;
    left: 270px;
    top: 0;
    width: 343px;
    height: 300px;
    background: radial-gradient(ellipse 60% 58% at 70% 42%, rgba(155,78,76,0.85) 0%, rgba(127,174,118,0.8) 55%, rgba(127,174,118,0) 100%);
  }
  .people {
    position: absolute;
    right: 378px;
    top: 76px;
    text-align: right;
    line-height: 21px;
    font-size: 15.5px;
    color: var(--maroon);
  }
  .person + .person { margin-top: 23px; }
  .person__name { color: var(--leaf-green); font-weight: 700; }
  .contact-line { display: flex; justify-content: flex-end; align-items: center; gap: 5px; }
  .icon { width: 12px; height: 12px; fill: var(--leaf-green); flex: none; }
  .web-details {
    position: absolute;
    right: 42px;
    top: 285px;
    font-size: 15.5px;
    line-height: 21px;
    color: var(--maroon);
  }
  .web-details .contact-line { gap: 9px; }
  .web-details .icon { width: 13px; height: 13px; }
  .brand {
    position: absolute;
    left: 0; right: 0;
    top: 214px;
    text-align: center;
  }
  .brand__name {
    font-size: 34px;
    font-weight: 400;
    color: var(--leaf-green);
    text-transform: uppercase;
    letter-spacing: 0.3px;
    line-height: 42px;
  }
  .brand__tagline {
    margin-top: 2px;
    font-size: 17px;
    color: var(--tag-green);
  }
  .brand__tagline .sep { color: var(--maroon); font-size: 12px; margin: 0 6px; vertical-align: 2px; }
</style>
</head>
<body>
  <section class="card card--front">
    <div class="front-artwork" role="img" aria-label="Large leafy tree decoration in soft green and brown"></div>
    <div class="people">
      <div class="person">
        <div class="person__name">Dr. Colin R. Haskell</div>
        <div class="person__quals">MBBS FRACGP</div>
        <div class="contact-line">
          <svg class="icon" viewBox="0 0 24 24"><path d="M6.6 10.8a15.1 15.1 0 0 0 6.6 6.6l2.2-2.2a1 1 0 0 1 1-.25 11.4 11.4 0 0 0 3.6.57 1 1 0 0 1 1 1V20a1 1 0 0 1-1 1A17 17 0 0 1 3 4a1 1 0 0 1 1-1h3.5a1 1 0 0 1 1 1c0 1.25.2 2.45.57 3.57a1 1 0 0 1-.25 1z"/></svg>
          <span>+61491578204</span>
        </div>
      </div>
      <div class="person">
        <div class="person__name">Dr. Paul Brennagh</div>
        <div class="person__quals">PhD MBusStrategy</div>
        <div class="contact-line">
          <svg class="icon" viewBox="0 0 24 24"><path d="M6.6 10.8a15.1 15.1 0 0 0 6.6 6.6l2.2-2.2a1 1 0 0 1 1-.25 11.4 11.4 0 0 0 3.6.57 1 1 0 0 1 1 1V20a1 1 0 0 1-1 1A17 17 0 0 1 3 4a1 1 0 0 1 1-1h3.5a1 1 0 0 1 1 1c0 1.25.2 2.45.57 3.57a1 1 0 0 1-.25 1z"/></svg>
          <span>+61472019847</span>
        </div>
      </div>
    </div>
    <div class="web-details">
      <div class="contact-line">
        <span>colin@brightwatermedical.com.au</span>
        <svg class="icon" viewBox="0 0 24 24"><path d="M2 5h20v14H2z" fill="none" stroke="#4b7f1f" stroke-width="2.5"/><path d="M2 5l10 8 10-8" fill="none" stroke="#4b7f1f" stroke-width="2.5"/></svg>
      </div>
      <div class="contact-line">
        <span>www.brightwatermedical.com.au</span>
        <svg class="icon" viewBox="0 0 24 24"><g fill="none" stroke="#4b7f1f" stroke-width="2.2"><circle cx="12" cy="12" r="10"/><ellipse cx="12" cy="12" rx="4.5" ry="10"/><path d="M2 12h20M4 7h16M4 17h16"/></g></svg>
      </div>
    </div>
  </section>

  <section class="card card--back">
    <div class="brand">
      <div class="brand__name">Brightwater Medical</div>
      <div class="brand__tagline">Insight<span class="sep">|</span>Implementation<span class="sep">|</span>Growth</div>
    </div>
  </section>
</body>
</html>
```